Staff Newsletter Template Image

We are looking for two .jpg images that we can put into a Word document and use for our staff newsletter. We will then add content using text boxes.
Attached is the current template which works for the columns and size that we need but we just want a fresh new design.
The Word document shows how we use it.
The name will stay the same - Team upBeat but can be a different look to the current one.

Target Market(s)

Sales team

Colors

Designer to choose colors to be used in the design.

Requirements
Must have
• Colours will be green, grey and white, possibly cream if needed. All from the guidelines.
• I have attached our brand guidelines which shows design elements and fonts for our brand. Also attached is brand guidelines for one of our product lines as we would like to use the same green.
• It needs to be nice to look at and motivational for our team

```html
<!DOCTYPE html>
<html lang="en">
<head>
<meta charset="utf-8">
<title>Team upBeat – Staff Newsletter</title>
<link rel="stylesheet" href="https://fonts.googleapis.com/css2?family=Montserrat:wght@400;600;700&display=swap">
<style>
  :root {
    --green: #8cc63f;
    --grey: #e6e6e6;
    --grey-fold: #d2d2d2;
    --white: #ffffff;
    --bronze: #8a6d4e;
    --frame: #a9d8f2;
    --ink: #333333;
  }
  html, body {
    margin: 0;
    padding: 0;
    overflow: hidden;
    background: var(--white);
  }
  .newsletter {
    position: relative;
    width: 851px;
    height: 1200px;
    overflow: hidden;
    background: var(--white);
    font-family: "Montserrat", Arial, sans-serif;
  }
  .backdrop {
    position: absolute;
    inset: 0;
  }
  .frame {
    position: absolute;
    inset: 2px;
    border: 2px solid var(--frame);
    pointer-events: none;
  }
  .team-name {
    position: absolute;
    left: 54px;
    top: 92px;
    margin: 0;
    font-weight: 600;
    font-size: 30px;
    line-height: 1;
    color: var(--bronze);
  }
  .product-line {
    position: absolute;
    right: 64px;
    top: 62px;
    margin: 0;
    font-weight: 700;
    font-size: 44px;
    line-height: 1;
    color: var(--white);
  }
  .footer-credit {
    position: absolute;
    left: 26px;
    bottom: 14px;
    margin: 0;
    font-size: 11px;
    color: var(--white);
  }
  .date-field {
    position: absolute;
    right: 24px;
    bottom: 10px;
    width: 160px;
    display: flex;
    align-items: flex-end;
    gap: 8px;
    font-size: 12px;
    font-weight: 600;
    color: var(--ink);
  }
  .date-field__line {
    flex: 1;
    border-bottom: 1px solid var(--ink);
    height: 12px;
  }
</style>
</head>
<body>
<main class="newsletter">
  <svg class="backdrop" width="851" height="1200" viewBox="0 0 851 1200" aria-hidden="true">
    <polygon class="band-grey" points="156,468 496,128 851,128 851,710 426,1200 300,1200" fill="var(--grey)"/>
    <polygon class="band-fold" points="851,710 600,1000 851,820" fill="var(--grey-fold)" opacity="0.6"/>
    <polygon class="band-green" points="0,610 156,468 681,950 426,1200 0,1200" fill="var(--green)"/>
    <polygon class="corner-green" points="326,0 851,0 851,142 732,261" fill="var(--green)"/>
  </svg>

  <h1 class="team-name">Team upBeat</h1>

  <p class="product-line">Greenleaf</p>

  <p class="footer-credit">© Oakline Wellness</p>

  <div class="date-field">
    <span>Date</span>
    <span class="date-field__line"></span>
  </div>

  <div class="frame"></div>
</main>
</body>
</html>
```